Mortgage broker flyer

I need a flyer to advertise who we are, what we do and why people should use us. and with a call to action. Our service is free, and we have over 35 different lenders that we can source loans from. we offer a mobile service. we will visit people anywhere anytime to discuss their needs. The flyers are to be placed in real estate agencies as well as put in people's letter boxes

Target Market(s)

clients looking at purchasing property - going through open homes.

Industry/Entity Type

Finance

Colors
add136
cadf82
aaaaaa
959595

Requirements
Must have
• Service is free
• won KRD broker of the year 2014,2015
• Veltrona insurance - Free 90 days building insurance through Veltrona
• Logo colours

```html
<!DOCTYPE html>
<html lang="en">
<head>
<meta charset="utf-8">
<title>Keyway Finance Solutions – Flyer</title>
<link rel="stylesheet" href="https://fonts.googleapis.com/css2?family=Lato:wght@400;700&family=Oswald:wght@500;600&family=Mulish:wght@500;600&display=swap">
<style>
  :root {
    --green: #4fae30;
    --green-light: #8fe46a;
    --green-mid: #add136;
    --navy: #13124a;
    --ink: #1d1d2e;
    --charcoal: #2b2b2b;
    --grey: #959595;
    --grey-light: #aaaaaa;
    --ring: #6a6a6a;
    --white: #ffffff;
  }
  * { box-sizing: border-box; margin: 0; padding: 0; }
  html, body { width: 902px; height: 1200px; overflow: hidden; background: #ffffff; }
  .flyer {
    position: relative; width: 902px; height: 1200px; overflow: hidden;
    background: var(--white); font-family: "Lato", sans-serif; color: var(--ink);
  }
  .top-bar { position: absolute; left: 0; top: 0; width: 100%; height: 20px; background: var(--navy); }
  .hero-photo {
    position: absolute; left: 0; top: 20px; width: 100%; height: 460px;
    background: linear-gradient(135deg, #cfdcec 0%, #eef3f8 40%, #b8c9dd 70%, #8fa6c0 100%);
  }
  .logo-tab { position: absolute; left: 22px; top: 20px; width: 296px; height: 116px; }
  .logo-tab svg { position: absolute; inset: 0; }
  .logo-lockup {
    position: absolute; left: 32px; top: 22px; display: flex; align-items: center; gap: 12px;
    color: var(--green); font-family: "Lato", sans-serif; font-weight: 400; font-size: 24px; line-height: 1.05;
  }
  .logo-mark { width: 36px; height: 36px; background: var(--green-mid); }
  .swoosh { position: absolute; left: 0; top: 340px; width: 902px; height: 140px; }

  .services { position: absolute; left: 26px; top: 474px; width: 345px; }
  .section-title { font-family: "Mulish", sans-serif; font-weight: 500; font-size: 22px; letter-spacing: 0.5px; color: var(--ink); }
  .services-list { list-style: none; margin-top: 22px; }
  .services-list li { position: relative; padding-left: 24px; font-size: 13.5px; line-height: 1.3; margin-bottom: 12px; }
  .services-list li::before {
    content: ""; position: absolute; left: 0; top: 4px; width: 11px; height: 11px; border-radius: 50%; background: var(--green);
  }
  .services-list li.plain::before { display: none; }

  .about {
    position: absolute; left: 391px; top: 420px; width: 511px; height: 376px;
    border-left: 4px solid var(--grey-light); border-bottom: 4px solid var(--grey-light);
    border-radius: 18px 0 0 48px; overflow: hidden;
  }
  .about-inner {
    width: 100%; height: 100%; padding: 22px 16px 0 22px; border-radius: 14px 0 0 44px;
    background: linear-gradient(180deg, var(--green) 0%, #6bd048 55%, var(--green-light) 100%);
  }
  .about .section-title { margin-left: 8px; margin-bottom: 14px; }
  .about p { font-size: 13.4px; line-height: 1.3; text-align: justify; color: var(--ink); margin-bottom: 10px; }

  .award-band {
    position: absolute; left: 336px; top: 843px; width: 566px; height: 160px;
    border-top: 6px solid var(--green); border-bottom: 6px solid var(--green);
    background: var(--charcoal); padding: 14px 0 0 31px;
    font-family: "Oswald", sans-serif; font-weight: 500; font-size: 26px; line-height: 1.35; color: var(--white);
  }
  .award-band .award { margin-bottom: 14px; }
  .award-band .insurer { color: var(--green); }

  .free-badge {
    position: absolute; left: 25px; top: 786px; width: 300px; height: 300px; border-radius: 50%;
    border: 10px solid var(--ring); background: var(--white); padding: 9px;
  }
  .free-badge-core {
    width: 100%; height: 100%; border-radius: 50%; background: var(--green);
    display: flex; flex-direction: column; align-items: center; justify-content: center;
    font-family: "Oswald", sans-serif; font-weight: 600; text-align: center;
  }
  .free-badge-core .lead { color: var(--white); font-size: 50px; line-height: 1; margin-top: -6px; }
  .free-badge-core .big { color: var(--charcoal); font-size: 100px; line-height: 1.05; letter-spacing: 2px; }

  .contact { position: absolute; left: 366px; top: 1038px; list-style: none; font-size: 15px; line-height: 1.25; color: var(--ink); }
  .contact li { display: flex; align-items: flex-start; gap: 16px; margin-bottom: 10px; }
  .contact svg { width: 14px; height: 14px; flex: none; margin-top: 2px; fill: var(--green); }

  .team-photo {
    position: absolute; left: 698px; top: 1000px; width: 144px; height: 158px;
    border: 4px solid var(--green);
    background: linear-gradient(180deg, #3a3a3a 0%, #1a1a1a 60%, #2c2c2c 100%);
  }

  .follow { position: absolute; left: 33px; top: 1116px; display: flex; align-items: center; gap: 14px; }
  .follow-label { font-weight: 700; font-size: 18px; color: var(--green); }
  .social { display: flex; align-items: center; gap: 6px; font-size: 15px; font-weight: 700; color: var(--ink); }
  .social-dot { width: 14px; height: 14px; border-radius: 50%; background: var(--ink); }

  .bottom-bar { position: absolute; left: 0; bottom: 0; width: 100%; height: 36px; background: var(--charcoal); }
</style>
</head>
<body>
<main class="flyer">
  <div class="top-bar"></div>
  <div class="hero-photo" role="img" aria-label="Photo of hands working with a calculator, notebook, laptop and financial charts on a desk"></div>

  <div class="logo-tab">
    <svg viewBox="0 0 296 116" width="296" height="116" aria-hidden="true">
      <polygon points="0,0 296,0 296,84 148,116 0,84" fill="#ffffff"/>
      <polyline points="0,80 148,112 296,80" fill="none" stroke="#4fae30" stroke-width="4"/>
      <polyline points="0,86 148,118 296,86" fill="none" stroke="#2b2b2b" stroke-width="3"/>
    </svg>
    <div class="logo-lockup">
      <span class="logo-mark"></span>
      <span>Keyway<br>Finance Solutions</span>
    </div>
  </div>

  <svg class="swoosh" viewBox="0 0 902 140" aria-hidden="true" preserveAspectRatio="none">
    <path d="M0,92 C300,20 650,22 902,34 L902,62 C650,52 320,62 0,112 Z" fill="#4fae30"/>
    <path d="M0,112 C320,62 650,52 902,62 L902,80 C650,72 380,78 0,128 Z" fill="#1b1b1b"/>
    <path d="M0,128 C380,78 650,72 902,80 L902,140 L0,140 Z" fill="#ffffff"/>
  </svg>

  <section class="services">
    <h2 class="section-title">OUR SERVICES</h2>
    <ul class="services-list">
      <li>Lorem ipsum dolor sit amet, consectetuer adipiscing elit. Aenean commodo ligula eget dolor.</li>
      <li>Aenean massa. Cum sociis natoque penatibus et magnis dis parturient montes, nascetur ridiculus mus.</li>
      <li>Donec quam felis, ultricies nec, pellentesque eu, pretium quis, sem.</li>
      <li>Nulla consequat massa quis enim. Donec pede justo, fringilla vel, aliquet nec, vulputate eget, arcu. In enim justo, rhoncus ut,</li>
      <li class="plain">Nullam dictum felis eu pede mollis pretium. Integer tincidunt.</li>
    </ul>
  </section>

  <section class="about">
    <div class="about-inner">
      <h2 class="section-title">ABOUT US</h2>
      <p>Keyway Finance Solutions is a Brisbane based mortgage brokerage. We understand that every client's financial situation is unique and therefore we take the time to know YOU and your financial goals.</p>
      <p>Our passion is assisting you in owning your property sooner! “Communication is the Key” we believe this is our point of difference. We take the time to explain the loan process from the initial consultation right through to settlement. Rest assured knowing you will be kept informed at each stage of the process.</p>
      <p>We realise how complex and time consuming it can be dealing with different banks. We eliminate this stress by shopping around for you. We have a panel of 36 lenders whom we compare hundreds of products and rates so that we can present you with the best home loan package.</p>
    </div>
  </section>

  <section class="award-band">
    <p class="award">Won KRD broker of the year 2014,2015</p>
    <p class="insurer">Veltrona insurance -</p>
    <p>Free 90 days building insurance through Veltrona</p>
  </section>

  <div class="free-badge">
    <div class="free-badge-core">
      <span class="lead">Service is</span>
      <span class="big">FREE</span>
    </div>
  </div>

  <ul class="contact">
    <li>
      <svg viewBox="0 0 14 14" aria-hidden="true"><path d="M7 1 L13 7 L11 7 L11 13 L8.5 13 L8.5 9 L5.5 9 L5.5 13 L3 13 L3 7 L1 7 Z"/></svg>
      <span>Po Box 1208, Ashgrove. QLD. 4060.<br>0400 123 987</span>
    </li>
    <li>
      <svg viewBox="0 0 14 14" aria-hidden="true"><path d="M1 3 H13 V11 H1 Z M1.5 3.5 L7 8 L12.5 3.5" stroke="#fff" stroke-width="0.8"/></svg>
      <span>info@keywayfs.com.au</span>
    </li>
    <li>
      <svg viewBox="0 0 14 14" aria-hidden="true"><circle cx="7" cy="7" r="6"/><path d="M1 7 H13 M7 1 C4 4 4 10 7 13 M7 1 C10 4 10 10 7 13" stroke="#fff" stroke-width="0.8" fill="none"/></svg>
      <span>www.keywayfs.com.au</span>
    </li>
  </ul>

  <div class="team-photo" role="img" aria-label="Photo of two brokers in formal suits holding an award"></div>

  <div class="follow">
    <span class="follow-label">Folow Us On</span>
    <span class="social"><span class="social-dot"></span>Chatterly</span>
    <span class="social"><span class="social-dot"></span>Postwave</span>
  </div>

  <div class="bottom-bar"></div>
</main>
</body>
</html>
```